Hello,
Corinne Haskett Equestrian needs a business card. We are a high performance show jumping stables based at Willowmere Reserve in morningotn. We pride ourselves on producing high quality show jumping horses and competing our stock at a high level. My business card need to have my logo on it, and i would like it to have a classic design with a modern touch. I would like it to have quite a natural feel about it. It needs to be in a font which is easy to read as I spend a lot of time competing internationally and overseas, and i need to be able to give it out to breeders and contacts where English isnt their first language. I will need it to include the following details:
-Corinne Haskett Equestrian
-Based at Willowmere Reserve Harrowgate
-Address: 17 Tremont Lane Harrowgate Westmark 3987
-Mobile number: 0412605948
- website: www.corinnehaskettequestrian.example
Target Market(s)
For business adults who english may not be their first language
Industry/Entity Type
Business

```html
<!DOCTYPE html>
<html lang="en">
<head>
<meta charset="utf-8">
<title>Corinne Haskett Equestrian — Business Card</title>
<link rel="stylesheet" href="https://fonts.googleapis.com/css2?family=Cinzel:wght@500&family=Tinos&display=swap">
<style>
  :root {
    --page: #f8f0da;
    --card: #fae4ae;
    --rust: #b65b29;
    --ink: #1d1b18;
  }
  * { margin: 0; padding: 0; box-sizing: border-box; }
  html, body {
    width: 1049px;
    height: 1200px;
    overflow: hidden;
    background: var(--page);
  }
  .sheet {
    position: relative;
    width: 1049px;
    height: 1200px;
  }
  .card {
    position: absolute;
    left: 132px;
    width: 785px;
    height: 449px;
    background: var(--card);
    overflow: hidden;
  }
  .card--front { top: 130px; }
  .card--back { top: 621px; }

  .brand-mark {
    position: absolute;
    left: 50%;
    top: 144px;
    width: 84px;
    height: 84px;
    margin-left: -42px;
    border-radius: 50%;
    background: var(--rust);
  }
  .brand-name {
    position: absolute;
    left: 0;
    right: 0;
    top: 270px;
    text-align: center;
    font-family: "Cinzel", serif;
    font-weight: 500;
    font-size: 29px;
    letter-spacing: 0.5px;
    color: var(--ink);
  }
  .corner {
    position: absolute;
    width: 195px;
    height: 175px;
  }
  .corner--front { left: 0; bottom: 0; }
  .corner--back { right: 0; bottom: 0; }

  .base {
    position: absolute;
    left: 407px;
    top: 36px;
    font-family: "Tinos", serif;
    font-size: 25px;
    line-height: 31px;
    color: var(--ink);
  }
  .contact {
    position: absolute;
    left: 28px;
    top: 322px;
    list-style: none;
    font-family: "Tinos", serif;
    font-size: 22px;
    line-height: 33px;
    color: var(--ink);
  }
</style>
</head>
<body>
  <main class="sheet">
    <section class="card card--front" aria-label="Card front">
      <div class="brand-mark" aria-hidden="true"></div>
      <h1 class="brand-name">Corinne Haskett Equestrian</h1>
      <svg class="corner corner--front" viewBox="0 0 195 175" role="img" aria-label="Decorative brand accent in rust">
        <path d="M0 0 A175 175 0 0 1 175 175 L0 175 Z" fill="var(--rust)"/>
      </svg>
    </section>

    <section class="card card--back" aria-label="Card back">
      <p class="base">Based at<br>Willowmere Reserve Harrowgate</p>
      <ul class="contact">
        <li>A : 17 Tremont Lane Harrowgate Westmark 3987</li>
        <li>M: 0412605948</li>
        <li>W: www.corinnehaskettequestrian.example</li>
      </ul>
      <svg class="corner corner--back" viewBox="0 0 195 175" role="img" aria-label="Decorative brand accent in rust">
        <path d="M195 0 A175 175 0 0 0 20 175 L195 175 Z" fill="var(--rust)"/>
      </svg>
    </section>
  </main>
</body>
</html>
```